Tavi wine label

Get all the info (Picture of another bottle & Logo) on a label on a thin wrap label, label size 1.5" width and 11-12" length. Also need Wine Name "TAVI" and grape varietal "Gamay" and "Alc. By Vol. 12.8%"

```html
<!DOCTYPE html>
<html lang="en">
<head>
<meta charset="utf-8">
<title>Tavi Estate Gamay – Wrap Label</title>
<link rel="stylesheet" href="https://fonts.googleapis.com/css2?family=Playfair+Display:ital,wght@0,400;0,700;0,800;1,400&display=swap">
<style>
  :root {
    --page-bg: #e0e0e0;
    --label-white: #ffffff;
    --guide-ink: #3a3a3a;
    --floral-dark: #1f1c1c;
    --floral-cream: #e9e2d2;
    --paper: #f1ebdf;
    --frame-rose: #c96a6f;
    --ink: #1a1818;
    --varietal-rose: #c24f5c;
    --estate-green: #8da62e;
  }
  * { box-sizing: border-box; margin: 0; padding: 0; }
  html, body {
    width: 1200px;
    height: 304px;
    overflow: hidden;
    background: var(--page-bg);
    font-family: "Playfair Display", Georgia, serif;
    color: var(--ink);
  }
  .canvas { position: relative; width: 1200px; height: 304px; }

  /* size guides */
  .guide-width {
    position: absolute; left: 86px; top: 53px; width: 1022px; height: 8px;
    border-left: 1px solid var(--guide-ink); border-right: 1px solid var(--guide-ink);
  }
  .guide-width::before {
    content: ""; position: absolute; left: 0; right: 0; top: 0; border-top: 1px solid var(--guide-ink);
  }
  .guide-width-text {
    position: absolute; left: 86px; width: 1022px; top: 38px; text-align: center;
    font-family: Arial, Helvetica, sans-serif; font-size: 12px; color: var(--guide-ink);
  }
  .guide-height {
    position: absolute; left: 66px; top: 74px; width: 8px; height: 164px;
    border-top: 1px solid var(--guide-ink); border-bottom: 1px solid var(--guide-ink);
  }
  .guide-height::before {
    content: ""; position: absolute; top: 0; bottom: 0; left: 6px; border-left: 1px solid var(--guide-ink);
  }
  .guide-height-text {
    position: absolute; left: 14px; top: 143px;
    font-family: Arial, Helvetica, sans-serif; font-size: 12px; color: var(--guide-ink);
  }

  /* label */
  .label {
    position: absolute; left: 86px; top: 74px; width: 1022px; height: 164px;
    background: var(--label-white);
    box-shadow: 0 0 1px rgba(0,0,0,.25);
  }
  .label-field {
    position: absolute; left: 12px; top: 10px; width: 1000px; height: 143px;
    overflow: hidden;
  }
  .floral-art {
    position: absolute; inset: 0;
    background:
      radial-gradient(circle at 12% 40%, var(--floral-cream) 0 8%, transparent 22%),
      radial-gradient(circle at 38% 70%, var(--floral-cream) 0 6%, transparent 20%),
      radial-gradient(circle at 62% 30%, var(--floral-cream) 0 7%, transparent 21%),
      radial-gradient(circle at 90% 65%, var(--floral-cream) 0 7%, transparent 20%),
      linear-gradient(90deg, #3a3533, var(--floral-dark) 50%, #3a3533);
  }

  .warning-card {
    position: absolute; left: 50px; top: 20px; width: 136px; height: 104px;
    background: var(--paper);
    transform: rotate(14deg);
    padding: 9px 7px;
    text-align: center;
    font-size: 6.8px; line-height: 1.2;
    color: var(--ink);
  }

  .title-card {
    position: absolute; left: 416px; top: -3px; width: 160px; height: 150px;
    background: var(--frame-rose);
    transform: rotate(10deg);
    padding: 6px;
  }
  .title-card-inner {
    width: 100%; height: 100%; background: var(--paper);
    display: flex; flex-direction: column; align-items: center; justify-content: center;
    text-align: center;
  }
  .wine-name { font-weight: 800; font-size: 34px; letter-spacing: 1px; line-height: 1; }
  .wine-estate { font-size: 11px; letter-spacing: 7px; margin-top: 1px; padding-left: 7px; }
  .wine-varietal { font-style: italic; color: var(--varietal-rose); font-size: 10.5px; letter-spacing: 3px; margin-top: 2px; }
  .wine-vintage { font-size: 8.5px; letter-spacing: 2px; margin-top: 1px; }
  .wine-abv { font-size: 7px; margin-top: 4px; }

  .producer-card {
    position: absolute; left: 806px; top: 20px; width: 120px; height: 96px;
    background: var(--paper);
    transform: rotate(14deg);
    display: flex; flex-direction: column; align-items: center; justify-content: center;
    text-align: center;
  }
  .producer-name { font-size: 14px; font-weight: 700; color: var(--estate-green); line-height: 1.1; margin-bottom: 6px; }
  .producer-details { font-size: 7px; line-height: 1.3; color: var(--ink); }
</style>
</head>
<body>
<div class="canvas">
  <div class="guide-width"></div>
  <div class="guide-width-text">11 in.</div>
  <div class="guide-height"></div>
  <div class="guide-height-text">1.75 in.</div>

  <section class="label">
    <div class="label-field">
      <div class="floral-art" role="img" aria-label="Engraved-style black and cream floral illustration of lotus, dahlia and leaves wrapping the full label"></div>

      <div class="warning-card">
        <p>GOVERNMENT WARNING:</p>
        <p>(1) According to the Surgeon General, women should not drink alcoholic beverages during pregnancy because of the risk of birth defects.</p>
        <p>(2) Consumption of alcoholic beverages impairs your ability to drive a car or operate machinery, and may cause health problems.</p>
      </div>

      <div class="title-card">
        <div class="title-card-inner">
          <h1 class="wine-name">TAVI</h1>
          <p class="wine-estate">ESTATE</p>
          <p class="wine-varietal">Gamay</p>
          <p class="wine-vintage">2017</p>
          <p class="wine-abv">Alc. By Vol. 12.8%</p>
        </div>
      </div>

      <div class="producer-card">
        <p class="producer-name">Hillside Acre</p>
        <p class="producer-details">Produced and Bottled By:<br>Hillside Acre, Millbrook, Ca<br>www.hillsideacre.com</p>
      </div>
    </div>
  </section>
</div>
</body>
</html>
```